Dunmore Plumbing LLC business card

Would like a modern looking business card with my new logo

Contact Information for Business Card

Calvin Dunmore 2418 Elm Hollow Rd Southbury, CT 06999, Dunmoreplumbingllc@exampletrade.com, 203-555-0174

```html
<!DOCTYPE html>
<html lang="en">
<head>
<meta charset="utf-8">
<title>Dunmore Plumbing LLC – Business Card</title>
<link href="https://fonts.googleapis.com/css2?family=Montserrat:wght@400;500;700;800&display=swap" rel="stylesheet">
<style>
  :root {
    --stage: #9a9a9a;
    --paper: #ffffff;
    --brand-blue: #29abe2;
    --ink: #1f1f1f;
    --faint: #f2f2f2;
  }
  * { margin: 0; padding: 0; box-sizing: border-box; }
  html, body { width: 1200px; height: 1059px; overflow: hidden; }
  body {
    position: relative;
    background: var(--stage);
    font-family: "Montserrat", sans-serif;
    color: var(--ink);
  }
  .card { position: absolute; overflow: hidden; }
  .card--front { left: 256px; top: 89px; width: 687px; height: 391px; background: var(--paper); }
  .card--back { left: 253px; top: 569px; width: 694px; height: 395px; background: var(--brand-blue); }

  .faucet-art {
    position: absolute; right: 0; top: 0; width: 265px; height: 235px;
    background: radial-gradient(ellipse at 60% 45%, var(--faint) 0%, rgba(242,242,242,0.6) 55%, rgba(255,255,255,0) 80%);
  }
  .wordmark { position: absolute; left: 34px; top: 58px; font-weight: 800; color: var(--ink); line-height: 1; }
  .wordmark__name { display: block; font-size: 43px; letter-spacing: 1px; }
  .wordmark__sub { display: block; font-size: 14px; letter-spacing: 3.2px; margin-top: 6px; text-align: center; }

  .holder-name {
    position: absolute; left: 34px; top: 309px; font-size: 26px; font-weight: 700;
    color: var(--brand-blue); letter-spacing: 0.4px;
  }
  .rule { position: absolute; left: 34px; top: 269px; width: 621px; height: 1px; background: var(--ink); }
  .holder-name { top: 223px; }

  .contact { position: absolute; left: 34px; top: 286px; display: flex; align-items: flex-end; font-size: 15px; font-weight: 400; }
  .contact__list { list-style: none; }
  .contact__item { display: flex; align-items: center; height: 24.5px; }
  .contact__icon { width: 13px; height: 13px; margin-right: 6px; fill: var(--brand-blue); flex: none; }
  .contact__divider { width: 1px; height: 40px; background: var(--brand-blue); margin: 0 14px 4px 16px; }
  .contact__address { font-style: normal; line-height: 22px; }

  .back-mark {
    position: absolute; left: 0; right: 0; top: 50%; transform: translateY(-50%);
    text-align: center; color: var(--paper); font-weight: 800; line-height: 1;
  }
  .back-mark__name { display: block; font-size: 78px; letter-spacing: 2px; }
  .back-mark__sub { display: block; font-size: 24px; letter-spacing: 5px; margin-top: 12px; }
</style>
</head>
<body>
  <section class="card card--front">
    <div class="faucet-art" role="img" aria-label="Faint large faucet illustration"></div>
    <div class="wordmark">
      <span class="wordmark__name">DUNMORE</span>
      <span class="wordmark__sub">PLUMBING LLC</span>
    </div>
    <h1 class="holder-name">CALVIN DUNMORE</h1>
    <div class="rule"></div>
    <div class="contact">
      <ul class="contact__list">
        <li class="contact__item">
          <svg class="contact__icon" viewBox="0 0 24 24"><path d="M6.6 10.8a15.1 15.1 0 0 0 6.6 6.6l2.2-2.2a1 1 0 0 1 1-.25 11.4 11.4 0 0 0 3.6.57 1 1 0 0 1 1 1V20a1 1 0 0 1-1 1A17 17 0 0 1 3 4a1 1 0 0 1 1-1h3.5a1 1 0 0 1 1 1c0 1.25.2 2.45.57 3.57a1 1 0 0 1-.25 1z"/></svg>
          203-555-0174
        </li>
        <li class="contact__item">
          <svg class="contact__icon" viewBox="0 0 24 24"><path d="M2 5h20v14H2z M2 5l10 8 10-8" fill="var(--brand-blue)" stroke="#fff" stroke-width="1.6"/></svg>
          Dunmoreplumbingllc@exampletrade.com
        </li>
        <li class="contact__item">
          <svg class="contact__icon" viewBox="0 0 24 24"><circle cx="12" cy="12" r="10"/><path d="M7 8c2 0 3 1 3 3s-2 2-2 4M15 5c-1 2 1 3 3 3M14 14c1 1 3 1 3 3" stroke="#fff" stroke-width="1.6" fill="none"/></svg>
          www.dunmoreplumbing.example
        </li>
      </ul>
      <span class="contact__divider"></span>
      <address class="contact__address">
        2418 Elm Hollow Rd<br>
        Southbury, CT 06999
      </address>
    </div>
  </section>

  <section class="card card--back">
    <div class="back-mark">
      <span class="back-mark__name">DUNMORE</span>
      <span class="back-mark__sub">PLUMBING LLC</span>
    </div>
  </section>
</body>
</html>
```